WPO Gel Nail Polish Collection for 15 ml bottle

We need a design for our new collection of WPO brand gel nail polish, called "SILK FOG". We are a nail salon / beauty supply distributor selling to retail nail salons in the US. Please look at the sample nail polish bottles attached for your reference. Our bottle will be white with a silver cap. Also, please look at our other project that is on HV for label design for the matching color tip swatches.

Target Market(s)

Retail Nail Salons in the US

Industry/Entity Type

Nail Salon

Colors

Designer to choose colors to be used in the design.

Requirements
Must have
• WPO logo - this needs to be changed to black color for letters WPO and matte gold for the "drop".
• PREMIUM GEL POLISH, SILK FOG, 0.5 oz (15 ml), back label wording.
• Front label wording must be clear and easy to read.
• Dimensions of label must be 1.125" x 4.0".
• Front part of label and back part of label must be spaced correctly so that they will be on opposite sides of the bottle.
Nice to have
• Color stripe possibly where the product name "SILK FOG" will appear, so that it stands out.
Should not have
• no actual pictures of SILK FOG, no overpowering graphics

```html
<!DOCTYPE html>
<html lang="en">
<head>
<meta charset="utf-8">
<title>WPO Silk Fog Premium Gel Polish – Label</title>
<link rel="stylesheet" href="https://fonts.googleapis.com/css2?family=Arimo:wght@400;700&family=Oswald:wght@600&display=swap">
<style>
  :root {
    --page-bg: #f3f3f3;
    --label-white: #ffffff;
    --label-edge: #e2e2e2;
    --ink: #111111;
    --ink-soft: #222222;
    --silver-dark: #9c9c9c;
    --silver-light: #cdcdcd;
    --accent-orange: #dc6a1f;
    --accent-orange-dark: #c25a17;
    --accent-gold: #d4922e;
    --drop-gold: #b89a55;
  }
  * { box-sizing: border-box; margin: 0; padding: 0; }
  html, body {
    width: 1200px; height: 1200px; overflow: hidden;
    background: var(--page-bg);
  }
  .canvas {
    width: 1200px; height: 1200px;
    display: flex; align-items: center; justify-content: center; gap: 44px;
  }
  .label-panel {
    width: 540px; height: 560px;
    background: linear-gradient(180deg, var(--label-white) 0%, #f4f4f4 100%);
    border: 1px solid var(--label-edge);
    border-radius: 14px;
    overflow: hidden;
    display: flex; flex-direction: column;
    font-family: "Arimo", Arial, sans-serif;
    color: var(--ink);
  }
  .panel-top {
    height: 220px;
    display: flex; align-items: center; justify-content: center;
  }
  .silver-band {
    height: 118px;
    background: linear-gradient(90deg, var(--silver-dark) 0%, var(--silver-light) 50%, var(--silver-dark) 100%);
    display: flex; align-items: center; justify-content: center; text-align: center;
  }
  .orange-band {
    height: 46px;
    background: linear-gradient(90deg, var(--accent-orange-dark) 0%, var(--accent-gold) 15%, var(--accent-orange) 40%, var(--accent-orange) 80%, var(--accent-orange-dark) 100%);
    display: flex; align-items: center; justify-content: center;
  }
  .panel-bottom {
    flex: 1;
    display: flex; align-items: center; justify-content: center; text-align: center;
    padding: 0 36px;
  }

  /* Front */
  .brand-mark { display: flex; align-items: center; gap: 10px; }
  .brand-name {
    font-family: "Arimo", Arial, sans-serif; font-weight: 700;
    font-size: 96px; letter-spacing: -2px; color: var(--ink); line-height: 1;
  }
  .brand-dot { width: 26px; height: 26px; border-radius: 50%; background: var(--drop-gold); }
  .product-name {
    font-family: "Oswald", "Arial Narrow", sans-serif; font-weight: 600;
    font-size: 66px; letter-spacing: 1px; color: var(--accent-orange);
  }
  .product-line { font-size: 24px; color: var(--ink); letter-spacing: 0.5px; }
  .net-volume { font-size: 30px; color: var(--ink-soft); }

  /* Back */
  .copy-block { text-align: center; padding: 0 44px; font-size: 18px; line-height: 1.32; color: var(--ink-soft); }
  .copy-heading { font-size: 19px; font-weight: 400; color: var(--ink); }
  .pro-notice { font-size: 26px; font-weight: 700; line-height: 1.3; color: var(--ink); letter-spacing: 0.3px; }
  .caution-block { font-size: 18px; line-height: 1.32; color: var(--ink-soft); }
</style>
</head>
<body>
<main class="canvas">
  <section class="label-panel label-front" aria-label="Front label">
    <div class="panel-top">
      <div class="brand-mark">
        <span class="brand-name">WPO</span>
        <span class="brand-dot" aria-hidden="true"></span>
      </div>
    </div>
    <div class="silver-band"><h1 class="product-name">SILK FOG</h1></div>
    <div class="orange-band"><p class="product-line">PREMIUM GEL POLISH</p></div>
    <div class="panel-bottom"><p class="net-volume">0.5 oz (15 ml)</p></div>
  </section>

  <section class="label-panel label-back" aria-label="Back label">
    <div class="panel-top">
      <div class="copy-block">
        <h2 class="copy-heading">DIRECTIONS FOR USE</h2>
        <p>Apply 1 coat over preferred gel polish base coat. Use magnet to create cat eye design after 2nd coat before curing with LED/UV light. Finish with preferred gel polish top coat. Must cure with LED/UV light after each coat. Approximate cure times: LED 30 seconds; UV 1-2 minutes.</p>
      </div>
    </div>
    <div class="silver-band"><p class="pro-notice">FOR PROFESSIONAL<br>USE ONLY</p></div>
    <div class="orange-band"></div>
    <div class="panel-bottom">
      <div class="caution-block">
        <h2 class="copy-heading">CAUTION</h2>
        <p>KEEP OUT OF REACH OF CHILDREN. Avoid skin contact. Discontinue use if sensitivity or irritation occurs. Avoid direct sunlight or exposure to extreme heat.</p>
      </div>
    </div>
  </section>
</main>
</body>
</html>
```